Design Simple & Basic Advertising Poster for Quivel and Dermal Filler

I need a few poster designs to display in a small salon, the services I wish to promote are Quivel and Dermal Filler. I am looking for something visually simple including a high quality picture, I have given an idea as to the type of image by attaching a few.

Text wise I would like to have some sort of prominent titling, something along the lines of "Quivel & Dermal Filler" and some text to say that it is available or is carried out at this salon. I am open two suggestions as to the text content but want it to be simple and to the point.

Please avoid anything pink, flowery or vivid colours. I am looking to keep it professional as it is a service at the upper end of cost for salons.

Please do not include any needles in the picture.

Impact is one of the key things I am looking for, something that strongly draws the eye.

```html
<!DOCTYPE html>
<html lang="en">
<head>
<meta charset="utf-8">
<title>Quivel &amp; Dermal Filler Posters</title>
<link rel="stylesheet" href="https://fonts.googleapis.com/css2?family=Barlow+Condensed:ital,wght@0,200;0,300;0,700;1,300;1,800&family=Barlow+Semi+Condensed:ital,wght@0,800;1,800&display=swap">
<style>
  :root {
    --backdrop: #e9e9ea;
    --skin-light: #d9b4a0;
    --skin-mid: #c69a83;
    --skin-deep: #8a5f4c;
    --hair: #241a16;
    --cream: #f6f0e2;
    --silver: #e4e4e4;
    --frame-line: rgba(235, 235, 235, 0.85);
  }
  * { margin: 0; padding: 0; box-sizing: border-box; }
  html, body {
    width: 1200px; height: 1200px; overflow: hidden;
    background: var(--backdrop);
  }
  .canvas { position: relative; width: 1200px; height: 1200px; }

  .poster { position: absolute; overflow: hidden; }
  .poster--italic { left: 23px; top: 47px; width: 570px; height: 806px; }
  .poster--upright { left: 612px; top: 377px; width: 568px; height: 803px; }

  .poster__photo {
    position: absolute; inset: 0;
    background:
      linear-gradient(90deg, transparent 44%, rgba(36,26,22,0.75) 50%, transparent 56%),
      linear-gradient(180deg, var(--hair) 0%, var(--skin-mid) 22%, var(--skin-light) 50%, var(--skin-mid) 78%, var(--skin-deep) 100%);
  }

  .headline {
    position: absolute; left: 0; right: 0;
    display: flex; flex-direction: column; align-items: center;
    text-align: center; line-height: 0.92;
  }

  .poster--italic .headline { top: 452px; left: 120px; right: 90px; color: var(--cream); font-style: italic; }
  .poster--italic .headline__light { font-family: "Barlow Condensed", sans-serif; font-weight: 300; }
  .poster--italic .headline__bold { font-family: "Barlow Semi Condensed", sans-serif; font-weight: 800; letter-spacing: -0.5px; }
  .poster--italic .headline__get { font-size: 40px; margin-left: -20px; }
  .poster--italic .headline__best { font-size: 66px; }
  .poster--italic .headline__service { font-size: 46px; margin-top: 4px; }
  .poster--italic .headline__product { font-size: 56px; }
  .poster--italic .headline__amp { font-size: 52px; }
  .poster--italic .headline__dermal { font-size: 58px; }

  .poster__frame {
    position: absolute; left: 21px; top: 16px; right: 20px; bottom: 15px;
    border: 3px solid var(--frame-line);
  }
  .poster--upright .headline { top: 322px; color: var(--silver); font-family: "Barlow Condensed", sans-serif; }
  .poster--upright .headline__get { font-size: 64px; font-weight: 300; color: #fff; }
  .poster--upright .headline__best { font-size: 62px; font-weight: 200; }
  .poster--upright .headline__bold { font-family: "Barlow Semi Condensed", sans-serif; font-weight: 800; font-style: normal; }
  .poster--upright .headline__product { font-size: 68px; }
  .poster--upright .headline__amp { font-size: 62px; }
  .poster--upright .headline__dermal { font-size: 66px; }
  .poster--upright .headline__service { font-size: 44px; font-weight: 200; margin-top: 6px; }
</style>
</head>
<body>
<main class="canvas">
  <section class="poster poster--italic">
    <div class="poster__photo" role="img" aria-label="Close-up photograph of two women's faces side by side, cheek to cheek, with dark hair and smooth skin"></div>
    <h1 class="headline">
      <span class="headline__light headline__get">Get</span>
      <span class="headline__light headline__best">The Best</span>
      <span class="headline__bold headline__product">QUIVEL</span>
      <span class="headline__bold headline__amp">&amp;</span>
      <span class="headline__bold headline__dermal">DERMAL</span>
      <span class="headline__bold headline__dermal">FILLER</span>
      <span class="headline__light headline__service">Service</span>
    </h1>
  </section>

  <section class="poster poster--upright">
    <div class="poster__photo" role="img" aria-label="Close-up photograph of two women's faces side by side, cheek to cheek, with dark hair and smooth skin"></div>
    <div class="poster__frame"></div>
    <h1 class="headline">
      <span class="headline__get">GET</span>
      <span class="headline__best">THE BEST</span>
      <span class="headline__bold headline__product">QUIVEL</span>
      <span class="headline__bold headline__amp">&amp;</span>
      <span class="headline__bold headline__dermal">DERMAL</span>
      <span class="headline__bold headline__dermal">FILLER</span>
      <span class="headline__service">SERVICE</span>
    </h1>
  </section>
</main>
</body>
</html>
```